Web interface for PC desktop app

We need an HTML design for our new PC software.

To get an idea of the project scope, please review the interface draft in the attached files. The screenshot shows almost all dialogs of our product.

Our product is software that allows users to replace static Windows wallpaper with live animated scenes. The program interface consists of a gallery where users can select and download animated scenes, as well as an information area with scene details and current desktop settings. The product will be distributed on the Vexlo platform among the gamer community.

For this project, you need to create an engaging and user-friendly interface using HTML and CSS in two color schemes (black and white). Additionally, you will need to create a colorized version of the main program icon in vector format (a draft of the program icon is attached), design all other program icons, including icons for the title bar, and redraw all other images according to your design style.

Project Requirements:
-Develop a comprehensive design for the application, including icons and images, in two color schemes: dark and light.
-Colorize our main program icon according to your design style.
-Create other UI icons in all sizes from 16x16 to 512x512 pixels, ensuring that other images are suitable for up to 4K monitors.
-Ensure all UI controls have styles for standard Windows states: normal, hovered, active, and disabled.

Deliverables:
-Final design in HTML and CSS format.
-Icons in ICO format.
-Images in PNG format.

• all interface elements, including the program title bar, coded in HTML and CSS.

```html
<!DOCTYPE html>
<html lang="en">
<head>
<meta charset="utf-8">
<title>Livora – Live Wallpapers</title>
<link href="https://fonts.googleapis.com/css2?family=Poppins:wght@400;500;600&display=swap" rel="stylesheet">
<style>
:root{
  --teal:#169d94;
  --orange:#f26a1b;
  --ink:#222;
  --muted:#555;
  --line:#dcdcdc;
  --page:#f4f4f4;
  --white:#fff;
  --star:#f7a21b;
  --placeholder:#cfd3d6;
}
*{box-sizing:border-box;margin:0;padding:0}
html,body{width:1200px;height:636px;overflow:hidden}
body{position:relative;background:var(--page);font-family:'Poppins',sans-serif;color:var(--ink);font-size:8.5px}
.abs{position:absolute}
.topbar{left:0;top:0;width:800px;height:41px;background:var(--white)}
.brand{left:26px;top:8px;display:flex;align-items:center;gap:6px;font-weight:600;font-size:12px;color:var(--muted)}
.brand-mark{width:28px;height:28px;border-radius:5px;background:#7b7b7b}
.top-actions{right:27px;top:14px;display:flex;align-items:center;gap:12px;font-size:8.5px;font-weight:500}
.toggle{width:10px;height:6px;border-radius:3px;background:var(--teal);position:relative;margin-right:-6px}
.toggle::after{content:"";position:absolute;right:1px;top:1px;width:4px;height:4px;border-radius:50%;background:#fff}
.panel{background:var(--white);border:1px solid var(--line)}
.tab{display:flex;align-items:center;gap:5px;font-size:9.5px}
.tab.active{color:var(--teal)}
.display-preview{background:var(--placeholder);border:1px solid #b9bec2}
.btn{border:1px solid var(--line);background:#f7f7f7;display:flex;align-items:center;justify-content:center;gap:5px;font-size:8.5px;color:var(--ink)}
.icon-btn{width:20px;height:20px;border:1px solid var(--line);background:#f7f7f7;display:flex;align-items:center;justify-content:center}
.label{font-weight:600}
.teal{color:var(--teal)}
.photo{border-radius:1px}
.caption{font-size:8.5px;color:var(--ink);letter-spacing:.2px}
.field{border:1px solid var(--line);background:#fff;height:24px;display:flex;align-items:center;justify-content:space-between;padding:0 6px;font-size:8px}
.arrows{font-size:6px;line-height:4px;display:flex;flex-direction:column;color:#222}
.primary{background:var(--teal);color:#fff;display:flex;align-items:center;justify-content:center;gap:6px;font-weight:500}
.dialog{box-shadow:0 2px 6px rgba(0,0,0,.12)}
</style>
</head>
<body>

<header class="abs topbar">
  <div class="abs brand"><span class="brand-mark"></span>Livora</div>
  <div class="abs top-actions">
    <span class="toggle"></span><span style="margin-left:6px">Light Mode</span>
    <svg width="9" height="10" viewBox="0 0 9 10"><path d="M4.5 1C2.8 1 2 2.3 2 4v2.5L1 8h7L7 6.5V4C7 2.3 6.2 1 4.5 1z" fill="#169d94"/><circle cx="4.5" cy="9" r="1" fill="#169d94"/></svg>
    <svg width="18" height="9" viewBox="0 0 18 9"><circle cx="4.5" cy="4.5" r="3.8" fill="none" stroke="#666" stroke-width="1"/><circle cx="4.5" cy="3.6" r="1.3" fill="#666"/><path d="M2.2 7.2c1-1.5 3.6-1.5 4.6 0" fill="#666"/><path d="M12 3.5l2 2 2-2" fill="none" stroke="#666" stroke-width="1"/></svg>
  </div>
</header>

<!-- Display panel -->
<section class="abs panel" style="left:26px;top:53px;width:264px;height:166px">
  <div class="abs tab active" style="left:14px;top:10px">
    <svg width="9" height="8" viewBox="0 0 9 8"><rect x=".5" y=".5" width="8" height="7" fill="none" stroke="#169d94"/><path d="M1.5 6l2-2 1.5 1.5 1.5-1 1.5 1.5" fill="none" stroke="#169d94"/></svg>Wallpapers</div>
  <div class="abs tab" style="left:99px;top:10px">
    <svg width="8" height="9" viewBox="0 0 8 9"><rect x="2.5" y=".5" width="5" height="6" fill="none" stroke="#169d94"/><path d="M.5 2.5v6h5" fill="none" stroke="#169d94"/></svg>Screensavers</div>
  <div class="abs" style="left:8px;top:27px;width:248px;height:1px;background:var(--line)"></div>
  <div class="abs" style="left:8px;top:26px;width:80px;height:2px;background:var(--teal)"></div>

  <div class="abs display-preview" role="img" aria-label="Preview of display 1 with its current wallpaper" style="left:14px;top:43px;width:100px;height:72px"></div>
  <div class="abs display-preview" role="img" aria-label="Preview of display 2 with its current wallpaper" style="left:128px;top:44px;width:95px;height:68px"></div>

  <div class="abs" style="left:10px;top:130px;font-size:8.5px"><span class="label">Display 2:</span> <span style="color:var(--orange)">Norvex N24HD</span></div>
  <div class="abs" style="left:10px;top:143px;font-size:8px;color:var(--muted)">Background: &lt;system settings&gt;</div>
  <div class="abs icon-btn" style="left:147px;top:133px"><svg width="9" height="9" viewBox="0 0 10 10"><circle cx="5" cy="5" r="3.2" fill="none" stroke="#555" stroke-width="2" stroke-dasharray="1.6 1"/><circle cx="5" cy="5" r="1" fill="#555"/></svg></div>
  <div class="abs icon-btn" style="left:174px;top:133px"><svg width="8" height="8"><path d="M1 0l7 4-7 4z" fill="#555"/></svg></div>
  <div class="abs icon-btn" style="left:201px;top:133px"><svg width="7" height="7"><rect width="7" height="7" fill="#555"/></svg></div>
  <div class="abs icon-btn" style="left:228px;top:133px"><svg width="7" height="7"><rect width="2.5" height="7" fill="#555"/><rect x="4.5" width="2.5" height="7" fill="#555"/></svg></div>
</section>

<!-- Details panel -->
<section class="abs panel" style="left:26px;top:231px;width:264px;height:381px">
  <div class="abs" style="left:10px;top:9px;font-size:9.5px"><span class="label">Name:</span> <span class="teal" style="font-weight:500">Shadow Hood</span></div>
  <div class="abs photo" role="img" aria-label="Hooded armored game character in a neon city" style="left:10px;top:32px;width:243px;height:117px;background:radial-gradient(circle at 50% 45%,#3a4a60 0%,#1c2230 45%,#3a1c2a 80%,#7a2a40 100%)"></div>
  <div class="abs btn" style="left:9px;top:163px;width:58px;height:26px"><svg width="8" height="9"><rect x="2.5" y=".5" width="5" height="6" fill="none" stroke="#169d94"/><path d="M.5 2.5v6h5" fill="none" stroke="#169d94"/></svg>Apply</div>
  <div class="abs btn" style="left:73px;top:163px;width:58px;height:26px"><svg width="9" height="9" viewBox="0 0 9 9"><path d="M7.5 3.5A3.2 3.2 0 0 0 1.5 3M1.5 5.5a3.2 3.2 0 0 0 6 .5" fill="none" stroke="#169d94" stroke-width="1.2"/><path d="M7.8 1v2.7H5.2M1.2 8V5.3h2.6" fill="none" stroke="#169d94" stroke-width="1.2"/></svg>Test</div>
  <div class="abs btn" style="left:137px;top:163px;width:65px;height:26px"><svg width="9" height="8"><path d="M4 1H1v6h3" fill="none" stroke="#169d94"/><path d="M3 4h5M6 2l2 2-2 2" fill="none" stroke="#169d94"/></svg>Uninstall</div>

  <div class="abs" role="img" aria-label="Author avatar" style="left:9px;top:202px;width:20px;height:20px;border-radius:50%;background:radial-gradient(#c9a24a,#6b5a3a)"></div>
  <div class="abs" style="left:36px;top:201px;line-height:12px;font-size:8px">
    <div class="label">Autor:</div><div>Pixel Atelier</div>
    <div class="label" style="margin-top:6px">Resolution:</div><div>3800 x 2400</div>
    <div class="label" style="margin-top:6px">Size:</div><div>#NaN MB</div>
    <div class="label" style="margin-top:6px">Rating:</div>
  </div>
  <svg class="abs" style="left:36px;top:301px" width="82" height="10" viewBox="0 0 82 10">
    <defs><path id="st" d="M5 .5l1.3 2.9 3.2.3-2.4 2.1.7 3.1L5 7.3 2.2 8.9l.7-3.1L.5 3.7l3.2-.3z"/></defs>
    <use href="#st" fill="#f7a21b"/><use href="#st" x="12.5" fill="#f7a21b"/><use href="#st" x="25" fill="#f7a21b"/><use href="#st" x="37.5" fill="#f7a21b"/><use href="#st" x="50" fill="none" stroke="#777" stroke-width=".7"/>
  </svg>
  <div class="abs" style="left:103px;top:297px;width:17px;height:17px;border-radius:50%;border:1px solid var(--line);background:#f7f7f7;display:flex;align-items:center;justify-content:center"><svg width="8" height="8" viewBox="0 0 8 8"><path d="M.5 3.5h1.5v4H.5zM2 3.5L4 .5c1 0 1 .8.8 2H7c.6 0 .8.5.6 1L6.8 7c-.1.3-.4.5-.7.5H2" fill="none" stroke="#333" stroke-width=".8"/></svg></div>
  <div class="abs" style="left:125px;top:297px;width:17px;height:17px;border-radius:50%;border:1px solid var(--line);background:#f7f7f7;display:flex;align-items:center;justify-content:center"><svg width="8" height="8" viewBox="0 0 8 8" style="transform:rotate(180deg)"><path d="M.5 3.5h1.5v4H.5zM2 3.5L4 .5c1 0 1 .8.8 2H7c.6 0 .8.5.6 1L6.8 7c-.1.3-.4.5-.7.5H2" fill="none" stroke="#333" stroke-width=".8"/></svg></div>

  <div class="abs primary" style="left:9px;top:333px;width:150px;height:25px;font-size:8.5px"><svg width="10" height="8" viewBox="0 0 10 8"><rect x="1.5" y=".5" width="7" height="5" fill="none" stroke="#fff"/><path d="M0 7.5h10" stroke="#fff"/></svg>Create your own wallpaper</div>
</section>

<!-- Gallery -->
<div class="abs panel tab active" style="left:307px;top:53px;width:86px;height:30px;border-bottom:none;justify-content:center;z-index:2">
  <svg width="10" height="10" viewBox="0 0 9 9"><path d="M7.5 3.5A3.2 3.2 0 0 0 1.5 3M1.5 5.5a3.2 3.2 0 0 0 6 .5" fill="none" stroke="#169d94" stroke-width="1.2"/><path d="M7.8 1v2.7H5.2M1.2 8V5.3h2.6" fill="none" stroke="#169d94" stroke-width="1.2"/></svg>Installed</div>
<div class="abs panel tab" style="left:398px;top:53px;width:107px;height:29px;justify-content:center;color:var(--muted)">
  <svg width="9" height="8" viewBox="0 0 9 8"><rect x=".5" y=".5" width="8" height="7" fill="none" stroke="#666"/><path d="M1.5 6l2-2 1.5 1.5 1.5-1 1.5 1.5" fill="none" stroke="#666"/></svg>Workshop LWMI</div>
<div class="abs icon-btn" style="left:729px;top:58px"><svg width="9" height="9" viewBox="0 0 10 10"><circle cx="5" cy="5" r="3.2" fill="none" stroke="#555" stroke-width="2" stroke-dasharray="1.6 1"/><circle cx="5" cy="5" r="1" fill="#555"/></svg></div>
<div class="abs icon-btn" style="left:754px;top:58px"><svg width="8" height="8"><circle cx="4" cy="4" r="4" fill="#555"/><rect x="3.4" y="3.3" width="1.2" height="3" fill="#fff"/><circle cx="4" cy="2" r=".7" fill="#fff"/></svg></div>

<section class="abs panel" style="left:307px;top:82px;width:471px;height:530px">
  <div class="abs field" style="left:6px;top:8px;width:134px;color:var(--ink)">Search wallpaper..</div>
  <div class="abs field" style="left:146px;top:8px;width:125px"><span></span><span class="arrows">▲<br>▼</span></div>
  <div class="abs field" style="left:276px;top:8px;width:94px">All<span class="arrows">▲<br>▼</span></div>
  <div class="abs field" style="left:371px;top:8px;width:91px">Top Rated<span class="arrows">▲<br>▼</span></div>

  <div class="abs photo" role="img" aria-label="Archer warrior overlooking a mountain bay" style="left:8px;top:42px;width:216px;height:126px;background:linear-gradient(120deg,#7a4a2a 0%,#5a8aa8 40%,#9cc3d8 70%,#c9a24a 100%)"></div>
  <div class="abs caption" style="left:8px;top:176px">Dawn of the Tomorrow</div>
  <div class="abs photo" role="img" aria-label="Space shuttle launching above the glowing earth" style="left:244px;top:42px;width:216px;height:126px;background:radial-gradient(ellipse at 50% 10%,#8fd3ff 0%,#1e5a9a 25%,#0a1a33 60%,#8a7a66 100%)"></div>
  <div class="abs caption" style="left:244px;top:176px">Spcae</div>

  <div class="abs photo" role="img" aria-label="Hooded wanderer before a desert temple" style="left:8px;top:195px;width:216px;height:126px;background:linear-gradient(#a9bfd0 0%,#c8b496 45%,#9a8266 75%,#d8c8a8 100%)"></div>
  <div class="abs caption" style="left:8px;top:329px">Dawn of the Tomorrow</div>
  <div class="abs photo" role="img" aria-label="Colorful nebula with stars" style="left:244px;top:195px;width:216px;height:126px;background:radial-gradient(circle at 55% 55%,#c86aa8 0%,#5a4a9a 40%,#1a1a3a 80%)"></div>
  <div class="abs caption" style="left:244px;top:329px">Spcae</div>

  <div class="abs photo" role="img" aria-label="Ladybug on a dandelion seed head" style="left:8px;top:354px;width:216px;height:126px;background:radial-gradient(circle at 35% 55%,#d8653a 0%,#6aa8a8 45%,#2a8a90 100%)"></div>
  <div class="abs caption" style="left:8px;top:488px">Dawn of the Tomorrow</div>
  <div class="abs photo" role="img" aria-label="Snowy mountain over a lake with red autumn leaves" style="left:244px;top:354px;width:216px;height:126px;background:linear-gradient(#c8202a 0%,#b8c4d8 35%,#8a92a8 55%,#3a4a66 100%)"></div>
  <div class="abs caption" style="left:244px;top:488px">Spcae</div>
</section>

<!-- Settings dialog -->
<section class="abs panel dialog" style="left:817px;top:41px;width:341px;height:198px">
  <div class="abs" style="left:9px;top:15px;font-size:12px;font-weight:500">Desktop Background Settings</div>
  <svg class="abs" style="left:317px;top:20px" width="12" height="10" viewBox="0 0 12 10"><rect x=".5" y=".5" width="11" height="9" fill="none" stroke="#666"/><path d="M4 3l4 4M8 3L4 7" stroke="#666" stroke-width="1.2"/></svg>
  <div class="abs" style="left:10px;top:55px;font-size:8.5px">Language:</div>
  <div class="abs field" style="left:61px;top:49px;width:74px;height:22px">English<span class="arrows">▲<br>▼</span></div>
  <div class="abs" style="left:10px;top:82px;font-size:8.5px">Theme</div>
  <div class="abs field" style="left:61px;top:77px;width:74px;height:22px">Dark<span class="arrows">▲<br>▼</span></div>
  <div class="abs" style="left:11px;top:127px;width:7px;height:7px;border:1px solid #333"></div>
  <div class="abs" style="left:28px;top:124px;font-size:8.5px">Run Live Wallpaper on Window Startup</div>
  <div class="abs primary" style="left:10px;top:151px;width:37px;height:21px;font-size:9px">Ok</div>
</section>

</body>
</html>
```